"Nail Care" Postcard

Hello,

We are looking to redesign our current post card. The target audience of this post card age is 50+. We will be mailing these postcards through Tamblo Cards.
The goal of the message is to remind them that it is time to get their (toe) nail care done.

Attached is our previous postcard.
Post card size: 4.2” x 5.5”
Backside of the postcards needs space for the mailing address and postage.
Our address and logo need to be present.
The message of the back of the postcard needs to be present as well.
Examples of stock images must come with the example.
Files preferred to be in TIFF or .ai

Thank you,
Dorian F.

```html
<!DOCTYPE html>
<html lang="en">
<head>
<meta charset="utf-8">
<title>Stridewell Foot &amp; Ankle – Nail Care Postcard</title>
<link href="https://fonts.googleapis.com/css2?family=Rubik:wght@500;700&family=Josefin+Sans:wght@400;600&display=swap" rel="stylesheet">
<style>
  :root{
    --teal:#4fbf9f;
    --teal-dark:#3aa987;
    --orange:#ef7c45;
    --ink:#1d1d1d;
    --card:#f3f3f2;
    --page:#ffffff;
  }
  *{box-sizing:border-box;margin:0;padding:0}
  html,body{width:848px;height:1200px;overflow:hidden;background:var(--page)}
  .canvas{position:relative;width:848px;height:1200px}
  .postcard{
    position:absolute;top:454px;width:376px;height:292px;overflow:hidden;
    background:linear-gradient(135deg,#fafafa 0%,var(--card) 40%,#ececeb 100%);
    box-shadow:0 6px 14px rgba(0,0,0,.28);
  }
  .postcard--front{left:36px}
  .postcard--back{left:436px}
  .shape{position:absolute;inset:0}
  .brand{position:absolute;display:flex;align-items:center;gap:6px}
  .brand__mark{border-radius:50%;background:var(--teal);flex:none}
  .brand__name{font-family:"Rubik",sans-serif;font-weight:500;color:var(--orange);line-height:1.02;text-transform:uppercase}
  .brand__name small{display:block;font-size:.42em;text-align:right}
  .front .brand{left:92px;top:26px}
  .front .brand__mark{width:44px;height:44px}
  .front .brand__name{font-size:17px}
  .tagline{position:absolute;font-family:"Rubik",sans-serif;font-weight:700;color:var(--orange)}
  .front .tagline{left:0;width:376px;padding-left:42px;text-align:center;top:90px;font-size:15px}
  .headline{position:absolute;left:15px;top:125px;font-family:"Rubik",sans-serif;font-weight:700;color:var(--teal);font-size:20.5px;line-height:1.25}
  .contact{position:absolute;left:14px;top:217px;font-family:"Josefin Sans",sans-serif;font-size:11.5px;color:var(--ink)}
  .contact li{list-style:none;display:flex;align-items:center;gap:6px;height:17px}
  .contact svg{width:12px;height:12px}
  .social{position:absolute;left:33px;top:257px;display:flex;align-items:center;gap:5px;font-family:"Josefin Sans",sans-serif;font-size:10px;color:var(--ink)}
  .social span.dot{width:16px;height:16px;border-radius:50%;background:var(--orange)}
  .back .brand{left:17px;top:17px}
  .back .brand__mark{width:32px;height:32px}
  .back .brand__name{font-size:11.5px}
  .back .tagline{left:161px;top:29px;font-size:10.5px}
  .address{position:absolute;left:17px;top:57px;font-family:"Josefin Sans",sans-serif;font-size:6.8px;line-height:1.3;color:var(--ink)}
  .message{position:absolute;left:17px;top:91px;font-family:"Rubik",sans-serif;font-weight:700;color:var(--orange);font-size:14.5px;line-height:1.22}
  .cta{position:absolute;left:18px;top:169px;font-family:"Rubik",sans-serif;font-weight:700;color:var(--teal);font-size:10px;line-height:1.3}
  .note{position:absolute;left:17px;top:201px;font-family:"Josefin Sans",sans-serif;font-size:6px;line-height:1.35;color:var(--ink)}
</style>
</head>
<body>
<main class="canvas">

  <section class="postcard postcard--front front">
    <svg class="shape" viewBox="0 0 376 292" aria-hidden="true">
      <path d="M0 0 H60 C40 30 50 70 30 100 C20 118 10 125 0 128 Z" fill="var(--teal)"/>
      <circle cx="320" cy="193" r="96" fill="none" stroke="var(--orange)" stroke-width="3"/>
      <defs>
        <linearGradient id="procedure" x1="0" y1="0" x2="1" y2="1">
          <stop offset="0" stop-color="#7c8fb0"/><stop offset=".5" stop-color="#d99a78"/><stop offset="1" stop-color="#3f8fd6"/>
        </linearGradient>
        <linearGradient id="compare" x1="0" y1="0" x2="1" y2="0">
          <stop offset="0" stop-color="#d99470"/><stop offset=".5" stop-color="#c9c9c9"/><stop offset="1" stop-color="#e2a380"/>
        </linearGradient>
      </defs>
      <circle cx="320" cy="193" r="94" fill="url(#procedure)" role="img" aria-label="Gloved hands trimming a toenail with a nail tool"/>
      <circle cx="224" cy="234" r="60" fill="var(--teal)"/>
      <circle cx="226" cy="232" r="58" fill="url(#compare)" role="img" aria-label="Before and after view of a treated big toenail"/>
    </svg>
    <div class="brand">
      <span class="brand__mark"></span>
      <p class="brand__name">Stridewell<br>Foot &amp; Ankle<small>stridewellfeet.com</small></p>
    </div>
    <p class="tagline">We keep you moving!</p>
    <h1 class="headline">Have your nails been<br>taken care of?</h1>
    <ul class="contact">
      <li><svg viewBox="0 0 12 12"><circle cx="6" cy="6" r="5.3" fill="none" stroke="var(--teal)"/><path d="M4 3.2l1 1.2-.6.7c.4.9 1 1.5 1.9 1.9l.7-.6 1.2 1-.6.9C5.9 8.6 3.6 6.3 3.3 4z" fill="var(--teal)"/></svg>(555) 014-0192</li>
      <li><svg viewBox="0 0 12 12"><g fill="none" stroke="var(--teal)" stroke-width=".8"><circle cx="6" cy="6" r="5.3"/><ellipse cx="6" cy="6" rx="2.2" ry="5.3"/><path d="M.7 6h10.6M1.6 3.5h8.8M1.6 8.5h8.8"/></g></svg>www.stridewellfeet.com</li>
    </ul>
    <div class="social"><span class="dot"></span>@stridewellfeet</div>
  </section>

  <section class="postcard postcard--back back">
    <svg class="shape" viewBox="0 0 376 292" aria-hidden="true">
      <path d="M0 230 C30 240 50 262 56 292 H0 Z" fill="var(--teal)"/>
    </svg>
    <div class="brand">
      <span class="brand__mark"></span>
      <p class="brand__name">Stridewell<br>Foot &amp; Ankle<small>stridewellfeet.com</small></p>
    </div>
    <p class="tagline">We keep you moving!</p>
    <p class="address">88 Harlow Court, Suite 210<br>Ashby, MD 20100</p>
    <h2 class="message">We are pleased to<br>inform you may be due<br>for your bimonthly<br>nail care!</h2>
    <p class="cta">Please call our office<br>to schedule your appointment.</p>
    <p class="note">*If you have received nail care within the past<br>two months, please disregard *</p>
  </section>

</main>
</body>
</html>
```